Stationary Package for New Bookkeeping Business

We need the following stationary designs:

- Business Card
- Letterhead
- With Comps
- Envelopes
- Paper Folder
- Email Signature

We will provide accounting and bookkeeping services to small business. We would like have the main color as blue and have a modern professional look.

Variations of colour and shades of blue welcome
Preference for deeper darker blue - navy

Variations of font in logo also welcome

Industry/Entity Type

Accounting

Requirements
Must have
• Rosalind
B.Bus (Accounting)
Registered BAS Agent

Phone 0491 382 207
Post PO Box 624 Wattlegrove NSW 2749

Email rosalind@corbettledger.com

Business Card to be bold and eye catching

Should not have
• Letter head to not have too much colour on it

```html
<!DOCTYPE html>
<html lang="en">
<head>
<meta charset="utf-8">
<title>Corbett Ledger – Stationery Package</title>
<link href="https://fonts.googleapis.com/css2?family=Questrial&family=Arimo:wght@400;700&family=Dancing+Script&display=swap" rel="stylesheet">
<style>
  :root {
    --navy: #0b56a0;
    --navy-deep: #084a8c;
    --grey: #7d7d7d;
    --paper: #ffffff;
    --stage: #eeeeee;
    --ink: #555555;
    --muted: #9a9a9a;
    --tint: #e9f1fa;
    --rose: #c0392b;
  }
  * { box-sizing: border-box; margin: 0; padding: 0; }
  html, body { width: 1200px; height: 882px; overflow: hidden; }
  body {
    background: radial-gradient(ellipse at 50% 40%, #fafafa 0%, var(--stage) 100%);
    font-family: "Arimo", Arial, sans-serif;
    position: relative;
    color: var(--ink);
  }
  .piece { position: absolute; background: var(--paper); box-shadow: 0 2px 8px rgba(0,0,0,.18); overflow: hidden; }

  /* Brand lockup */
  .brand { display: flex; align-items: center; gap: 6px; font-family: "Questrial", sans-serif; color: var(--navy); line-height: .95; }
  .brand__mark { background: var(--grey); flex: none; }
  .brand--light { color: #fff; }
  .brand--light .brand__mark { background: #fff; }

  .hero-brand { left: 965px; top: 44px; position: absolute; font-size: 23px; }
  .hero-brand .brand__mark { width: 40px; height: 40px; }

  /* Letterhead */
  .letterhead { left: 40px; top: 80px; width: 340px; height: 460px; }
  .letterhead__corner { position: absolute; left: 0; top: 8px; width: 62px; height: 62px; background: var(--tint); }
  .letterhead .brand { position: absolute; right: 26px; top: 40px; font-size: 11px; }
  .letterhead .brand__mark { width: 18px; height: 18px; }
  .letterhead__body { position: absolute; left: 34px; right: 30px; top: 150px; font-size: 6.4px; line-height: 1.75; color: var(--muted); }
  .letterhead__body p:first-child { color: var(--ink); margin-bottom: 4px; }
  .letterhead__sign { position: absolute; left: 34px; top: 380px; font-size: 6px; color: var(--ink); }
  .letterhead__sign span { display: block; font-family: "Dancing Script", cursive; font-size: 14px; margin-top: 2px; }
  .letterhead__footer { position: absolute; left: 0; right: 0; bottom: 0; height: 20px; background: var(--navy); color: #fff; font-size: 5px; display: flex; justify-content: center; align-items: center; gap: 14px; }

  /* Business cards */
  .card { top: 140px; width: 170px; height: 100px; }
  .card--front { left: 476px; background: linear-gradient(135deg, #ffffff, #e6e6e6); display: flex; align-items: center; justify-content: center; }
  .card--front .brand { font-size: 12px; }
  .card--front .brand__mark { width: 20px; height: 20px; }
  .card--back { left: 656px; background: var(--navy); color: #fff; }
  .card__corner { position: absolute; left: 0; top: 0; width: 42px; height: 42px; background: rgba(255,255,255,.12); }
  .card__name { position: absolute; left: 56px; top: 22px; font-size: 7px; font-weight: 700; }
  .card__title { position: absolute; left: 56px; top: 31px; font-size: 4.5px; opacity: .85; }
  .contact { position: absolute; font-size: 4.5px; line-height: 1.6; }
  .contact__head { font-weight: 700; }
  .contact__row { display: flex; align-items: center; gap: 3px; }
  .contact__icon { width: 5px; height: 5px; flex: none; }
  .card--back .contact { left: 56px; top: 58px; }

  /* Compliments slip */
  .comp { left: 915px; top: 135px; width: 205px; height: 150px; }
  .comp .brand { position: absolute; right: 12px; top: 16px; font-size: 9px; }
  .comp .brand__mark { width: 14px; height: 14px; }
  .comp__with { position: absolute; left: 12px; top: 58px; font-family: "Dancing Script", cursive; font-size: 10px; color: var(--rose); }
  .comp__details { position: absolute; left: 12px; top: 74px; font-size: 4.5px; line-height: 1.6; color: var(--ink); }
  .comp__details b { font-size: 6px; color: var(--navy); }
  .comp__photo { position: absolute; right: 0; bottom: 0; width: 100px; height: 70px; background: radial-gradient(circle at 45% 60%, #f06b8a 0%, #f4a3b4 35%, #c9d9a8 65%, #ffffff 100%); }

  /* Envelopes */
  .envelope { width: 280px; }
  .envelope--back { left: 85px; top: 565px; height: 128px; }
  .envelope__flap { position: absolute; left: 0; top: 0; bottom: 0; width: 22px; background: var(--navy); }
  .envelope--back .brand { position: absolute; left: 100px; top: 42px; font-size: 9px; }
  .envelope--back .brand__mark { width: 14px; height: 14px; }
  .envelope--back .contact { left: 100px; top: 72px; color: var(--ink); }
  .envelope--front { left: 120px; top: 655px; height: 150px; width: 290px; }
  .envelope__corner { position: absolute; left: 0; top: 14px; width: 46px; height: 46px; background: var(--tint); }
  .envelope__to { position: absolute; left: 110px; top: 60px; font-size: 9px; line-height: 1.35; color: #b0b0b0; }

  /* Presentation folder */
  .folder { left: 483px; top: 340px; width: 646px; height: 458px; display: flex; }
  .folder__cover { position: relative; width: 323px; height: 100%; background: var(--navy); display: flex; align-items: center; justify-content: center; }
  .folder__cover .brand { font-size: 20px; }
  .folder__cover .brand__mark { width: 32px; height: 32px; }
  .folder__notch { position: absolute; right: -30px; top: 62px; width: 60px; height: 76px; border-radius: 50%; background: var(--paper); }
  .folder__inside { position: relative; width: 323px; height: 100%; background: var(--paper); }
  .folder__sheet { position: absolute; left: 16px; right: 16px; top: 24px; bottom: 24px; background: radial-gradient(ellipse at 50% 45%, #ffffff 0%, #dde9f5 100%); }
  .folder__card { position: absolute; left: 107px; top: 112px; width: 92px; height: 220px; background: var(--navy); display: flex; align-items: center; justify-content: center; }
  .folder__card .brand { font-size: 7px; }
  .folder__card .brand__mark { width: 10px; height: 10px; }
  .folder__pocket { position: absolute; left: 10px; right: 0; bottom: 0; height: 80px; background: var(--navy); border-top-left-radius: 22px; }
</style>
</head>
<body>

  <div class="brand hero-brand"><span class="brand__mark"></span><span>Corbett<br>Ledger</span></div>

  <!-- Letterhead -->
  <section class="piece letterhead">
    <div class="letterhead__corner"></div>
    <div class="brand"><span class="brand__mark"></span><span>Corbett<br>Ledger</span></div>
    <div class="letterhead__body">
      <p>Dear Sir,</p>
      <p>Thank you for choosing our practice for your bookkeeping needs. We look forward to helping your business keep clear, accurate records throughout the year. Our team will prepare your monthly reports, reconcile accounts and lodge your activity statements on time. Please contact us with any questions about your accounts, payroll or upcoming deadlines. We value your trust and support.</p>
    </div>
    <div class="letterhead__sign">From<span>Tom</span></div>
    <footer class="letterhead__footer">
      <span>Ph : 0491 382 207</span><span>|</span>
      <span>Post PO Box 624 Wattlegrove NSW 2749</span><span>|</span>
      <span>Email : rosalind@corbettledger.com</span>
    </footer>
  </section>

  <!-- Business card front -->
  <section class="piece card card--front">
    <div class="brand"><span class="brand__mark"></span><span>Corbett<br>Ledger</span></div>
  </section>

  <!-- Business card back -->
  <section class="piece card card--back">
    <div class="card__corner"></div>
    <div class="card__name">Rosalind</div>
    <div class="card__title">B.Bus (Accounting)</div>
    <div class="contact">
      <div class="contact__head">Registered BAS Agent</div>
      <div class="contact__row"><svg class="contact__icon" viewBox="0 0 5 5"><rect width="5" height="5" fill="#fff"/><path d="M1.2 1h1l.3 1-.5.4a2 2 0 0 0 .8.8l.4-.5 1 .3v1A3 3 0 0 1 1.2 1z" fill="#0b56a0"/></svg>0491 382 207</div>
      <div class="contact__row"><svg class="contact__icon" viewBox="0 0 5 5"><rect width="5" height="5" fill="#fff"/><rect x="1.2" y="1" width="2.6" height="3" fill="#0b56a0"/></svg>Post PO Box 624 Wattlegrove NSW 2749</div>
      <div class="contact__row"><svg class="contact__icon" viewBox="0 0 5 5"><rect width="5" height="5" fill="#fff"/><rect x="1" y="1.5" width="3" height="2" fill="#0b56a0"/></svg>rosalind@corbettledger.com</div>
    </div>
  </section>

  <!-- Compliments slip -->
  <section class="piece comp">
    <div class="brand"><span class="brand__mark"></span><span>Corbett<br>Ledger</span></div>
    <div class="comp__with">With Best Compliment From :</div>
    <div class="comp__details">
      <b>Corbett Ledger</b><br>
      Ph : 0491 382 207<br>
      Post PO Box 624 Wattlegrove NSW 2749<br>
      Email : rosalind@corbettledger.com
    </div>
    <div class="comp__photo" role="img" aria-label="Photograph of pink gerbera flowers with green leaves"></div>
  </section>

  <!-- Envelope back -->
  <section class="piece envelope envelope--back">
    <div class="envelope__flap"></div>
    <div class="brand"><span class="brand__mark"></span><span>Corbett<br>Ledger</span></div>
    <div class="contact">
      <div class="contact__head">Registered BAS Agent</div>
      <div class="contact__row"><svg class="contact__icon" viewBox="0 0 5 5"><rect width="5" height="5" fill="#0b56a0"/></svg>0491 382 207</div>
      <div class="contact__row"><svg class="contact__icon" viewBox="0 0 5 5"><rect width="5" height="5" fill="#0b56a0"/></svg>Post PO Box 624 Wattlegrove NSW 2749</div>
      <div class="contact__row"><svg class="contact__icon" viewBox="0 0 5 5"><rect width="5" height="5" fill="#0b56a0"/></svg>rosalind@corbettledger.com</div>
    </div>
  </section>

  <!-- Envelope front -->
  <section class="piece envelope envelope--front">
    <div class="envelope__corner"></div>
    <div class="envelope__to">To<br>Mr. Daniel Hartley<br># 2217, Sector - 18<br>Ballarat</div>
  </section>

  <!-- Presentation folder -->
  <section class="piece folder">
    <div class="folder__cover">
      <div class="brand brand--light"><span class="brand__mark"></span><span>Corbett<br>Ledger</span></div>
    </div>
    <div class="folder__inside">
      <div class="folder__sheet"></div>
      <div class="folder__card">
        <div class="brand brand--light"><span class="brand__mark"></span><span>Corbett<br>Ledger</span></div>
      </div>
      <div class="folder__pocket"></div>
    </div>
    <div class="folder__notch" style="left:293px; right:auto;"></div>
  </section>

</body>
</html>
```